Digital Marketing Website Design

I need the homepage designed for my new digital marketing agency I am starting. The main goal for this homepage is to drive people to make an appointment for me to discuss their upcoming projects. Here are some examples of the layouts that I would like to emulate.
https://www.tallorchard.com/
https://www.webmerchantry.com/
https://talewick.com/
https://drmevorran.com/
https://www.neatlynestled.org/
My main focus is to attract leads that need help with running digital ads such as Chatterbook ads and Quorix Ads. I do offer other services like SEO and other things but the main focus is digital Ads.
The final design should communicate Ember Pixelry is a Digital marketing strategist building predictable revenue for small businesses through digital ads, email and marketing automation.
Target Market(s)
30-55, business owners, income 100K+, ecommerce companies, etc.
Industry/Entity Type
Digital Marketing
Number of Pages Required
2 page
Requirements
Must have
- An appealing look and feel set to drive people to make an appointment.
There needs to be a call to action button in the far right of the navigation
The same call to action in the navigation needs to be in each section on the homepage.
I need the homepage and an about us page.

```html
<!DOCTYPE html>
<html lang="en">
<head>
<meta charset="utf-8">
<title>Ember Pixelry — Digital Ads for Small Businesses</title>
<link rel="stylesheet" href="https://fonts.googleapis.com/css2?family=Exo+2:wght@500;600;700&family=Poppins:wght@300;400;500&family=Roboto+Condensed:wght@400&display=swap">
<style>
:root{
  --navy:#0f2a5c;
  --hero-deep:#06123f;
  --hero-mid:#0a2f9a;
  --hero-glow:#1f6cff;
  --orange:#f15a24;
  --orange-dark:#d9431a;
  --ink:#2b2b33;
  --muted:#55565e;
  --blue:#1b97d5;
  --green:#6dbb3f;
  --yellow:#f8b616;
  --footer:#151a22;
  --band:#e63c2a;
  --white:#ffffff;
}
*{margin:0;padding:0;box-sizing:border-box}
html,body{width:1200px;height:2685px;overflow:hidden}
body{position:relative;font-family:"Poppins",sans-serif;color:var(--ink);background:var(--white)}
.abs{position:absolute}
.head-font{font-family:"Exo 2",sans-serif}

/* hero */
.hero{position:absolute;left:0;top:0;width:1200px;height:630px;
  background:radial-gradient(ellipse at 75% 40%,#2452d6 0%,var(--hero-mid) 35%,var(--hero-deep) 100%)}
.hero-art{position:absolute;left:0;top:140px;width:460px;height:440px;
  background:radial-gradient(circle at 52% 45%,#5fc4ff 0%,#1e74e8 32%,#0c3aa8 55%,rgba(10,40,140,0) 72%)}
.brand{position:absolute;font-family:"Exo 2",sans-serif;font-weight:700;color:var(--white);letter-spacing:1px}
.brand-dot{display:inline-block;width:14px;height:14px;border-radius:50%;background:var(--orange);margin-right:8px;vertical-align:middle}
.nav a{position:absolute;top:42px;font-family:"Exo 2",sans-serif;font-weight:600;font-size:19px;color:var(--white);text-decoration:none}
.nav a.active{color:var(--orange)}
.btn{position:absolute;display:flex;align-items:center;justify-content:center;background:var(--orange);color:var(--white);
  font-family:"Exo 2",sans-serif;font-weight:600;border-radius:3px;text-decoration:none}
.btn.dark{background:#050a1e;color:var(--orange)}
.hero-title{position:absolute;right:142px;top:236px;text-align:right;color:var(--white);font-family:"Exo 2",sans-serif;font-weight:600;font-size:32px;line-height:37px}
.hero-sub{position:absolute;right:142px;top:316px;text-align:right;color:var(--white);font-family:"Exo 2",sans-serif;font-weight:500;font-size:20px;line-height:28px}

/* sections */
.section-title{position:absolute;left:0;width:1200px;text-align:center;font-family:"Exo 2",sans-serif;font-weight:600;font-size:34px;color:var(--navy)}
.rule{position:absolute;left:565px;width:70px;height:3px;background:var(--orange)}
.para{position:absolute;left:150px;width:900px;text-align:center;font-size:15.5px;line-height:25px;color:var(--muted)}
.kicker{position:absolute;left:0;width:1200px;text-align:center;font-family:"Exo 2",sans-serif;font-weight:600;font-size:17px;color:var(--orange)}
.step-text{position:absolute;width:270px;text-align:center;font-size:14.5px;line-height:23px;color:var(--muted)}

/* testimonials */
.reviews{position:absolute;left:0;top:1449px;width:1200px;height:602px;
  background:linear-gradient(100deg,#1a1d24 0%,#2c3038 45%,#3a3f48 70%,#1c1f26 100%)}
.card{position:absolute;background:var(--white);overflow:hidden;box-shadow:0 4px 14px rgba(0,0,0,.35)}
.card .quote{position:absolute;left:10px;top:6px;font-family:"Exo 2",sans-serif;font-size:64px;line-height:64px;color:#d7d7d7}
.card p{position:absolute;left:12px;right:12px;top:38px;text-align:center;font-size:11.6px;line-height:18px;color:#444}
.card svg.wave{position:absolute;left:0;bottom:0}
.avatar{position:absolute;width:66px;height:66px;border-radius:50%;border:4px solid var(--white);background:#b9a89a}
.card .name{position:absolute;left:0;right:0;text-align:center;color:var(--white);font-weight:500;font-size:16px}
.card .co{position:absolute;left:0;right:0;text-align:center;color:var(--white);font-size:11px}
.slider-btn{position:absolute;width:42px;height:42px;border-radius:50%;display:flex;align-items:center;justify-content:center;font-size:12px}

/* featured */
.feature-box{position:absolute;top:2193px;width:129px;height:79px;background:var(--white);box-shadow:0 2px 10px rgba(0,0,0,.12);
  display:flex;align-items:center;justify-content:center;font-weight:500;font-size:16px;color:#555}

/* footer */
.footer{position:absolute;left:0;top:2351px;width:1200px;height:295px;
  background:linear-gradient(180deg,#1b2029 0%,#11151c 60%,#0d1016 100%)}
.foot-h{position:absolute;top:2416px;font-family:"Roboto Condensed",sans-serif;font-size:20px;color:var(--white)}
.foot-link{position:absolute;font-size:13px;color:var(--white)}
.band{position:absolute;left:0;top:2646px;width:1200px;height:39px;background:var(--band);color:var(--white);
  font-size:13px;display:flex;align-items:center;justify-content:center}
.social{position:absolute;top:2532px;width:24px;height:24px;border-radius:50%;border:2px solid var(--orange)}
</style>
</head>
<body>

<!-- HERO -->
<header class="hero">
  <div class="hero-art" role="img" aria-label="Glowing digital sphere of marketing icons held above an open hand"></div>
  <div class="brand" style="left:110px;top:38px;font-size:30px"><span class="brand-dot"></span>EMBERPIXELRY</div>
  <nav class="nav">
    <a class="active" style="left:493px">Home</a>
    <a style="left:584px">About Us</a>
    <a style="left:705px">Case Studies</a>
  </nav>
  <a class="btn" style="left:839px;top:34px;width:254px;height:41px;font-size:19px">Schedule Appointment</a>

  <h1 class="hero-title">We Built Profitable Ad Campaigns<br>For small businesses</h1>
  <p class="hero-sub">The Selling System That Brings In Predictable<br>Revenue Through Digital Ads, Email And<br>Marketing Automation</p>
  <a class="btn" style="left:521px;top:412px;width:290px;height:41px;font-size:18px">Free Chatterbook Ads Checklist</a>
  <a class="btn dark" style="left:825px;top:412px;width:234px;height:41px;font-size:18px">Schedule Appointment</a>
</header>

<!-- HOW IT WORKS -->
<section>
  <h2 class="section-title" style="top:696px">How It Works</h2>
  <div class="rule" style="top:747px"></div>
  <p class="para" style="top:768px">At Ember Pixelry we know that you want to have a profitable business. In order to do that, you need a strong system that can predictably bring in sales even in bad times. The problem is there is so much out there to wade through and so many people telling you what you should do which makes you feel frustrated, lost, and flat out stressed out. We believe that businesses with great products should get the customer.</p>
  <p class="para" style="top:874px">We understand the frustration which is why we are here to help you maneuver through the minutiae and create a system that flat out works.</p>
  <div class="kicker" style="top:938px">Here's How We Do It:</div>

  <svg class="abs" style="left:0;top:975px" width="1200" height="150" viewBox="0 975 1200 150">
    <defs>
      <radialGradient id="stepFill" cx="50%" cy="40%" r="60%">
        <stop offset="0%" stop-color="#ffffff"/><stop offset="100%" stop-color="#e4e4e6"/>
      </radialGradient>
    </defs>
    <g fill="none" stroke="var(--orange)" stroke-width="2">
      <path d="M238 1018 A60 60 0 0 1 350 1030"/><path d="M353 1058 A60 60 0 0 1 268 1102"/>
      <path d="M547 1018 A60 60 0 0 1 659 1030"/><path d="M662 1058 A60 60 0 0 1 577 1102"/>
      <path d="M856 1018 A60 60 0 0 1 968 1030"/><path d="M971 1058 A60 60 0 0 1 886 1102"/>
    </g>
    <circle cx="297" cy="1048" r="55" fill="url(#stepFill)"/>
    <circle cx="606" cy="1048" r="55" fill="url(#stepFill)"/>
    <circle cx="915" cy="1048" r="55" fill="url(#stepFill)"/>
    <!-- calendar -->
    <g fill="none" stroke="#3a3a40" stroke-width="1.8">
      <rect x="270" y="1025" width="50" height="42" rx="3"/><line x1="270" y1="1036" x2="320" y2="1036"/>
      <line x1="280" y1="1020" x2="280" y2="1030"/><line x1="296" y1="1020" x2="296" y2="1030"/><line x1="310" y1="1020" x2="310" y2="1030"/>
      <path d="M284 1052 l7 7 l13 -13"/><circle cx="316" cy="1064" r="9"/>
    </g>
    <!-- bulb and team -->
    <g fill="none" stroke="#3a3a40" stroke-width="1.8">
      <circle cx="606" cy="1028" r="10"/><path d="M601 1040 h10 M602 1045 h8"/>
      <path d="M606 1048 v6 M588 1058 h36 M588 1058 v4 M606 1054 v8 M624 1058 v4"/>
      <circle cx="588" cy="1066" r="4"/><circle cx="606" cy="1066" r="4"/><circle cx="624" cy="1066" r="4"/>
      <path d="M580 1078 a8 7 0 0 1 16 0 M598 1078 a8 7 0 0 1 16 0 M616 1078 a8 7 0 0 1 16 0"/>
    </g>
    <!-- growth with coins -->
    <g fill="none" stroke="#3a3a40" stroke-width="1.8">
      <path d="M893 1080 v-38 M888 1046 l5 -6 l5 6 M937 1080 v-38 M932 1046 l5 -6 l5 6"/>
      <circle cx="915" cy="1030" r="5"/><path d="M906 1060 v-20 h18 v20"/>
      <circle cx="900" cy="1074" r="7"/><circle cx="930" cy="1074" r="7"/>
    </g>
    <circle cx="240" cy="1074" r="15" fill="#111"/><text x="240" y="1079" text-anchor="middle" fill="var(--orange)" font-family="Poppins" font-size="14">1</text>
    <circle cx="550" cy="1073" r="15" fill="#111"/><text x="550" y="1078" text-anchor="middle" fill="var(--orange)" font-family="Poppins" font-size="14">2</text>
    <circle cx="859" cy="1074" r="15" fill="#111"/><text x="859" y="1079" text-anchor="middle" fill="var(--orange)" font-family="Poppins" font-size="14">3</text>
    <g stroke="#9a9aa0" stroke-width="1" stroke-dasharray="3 3"><line x1="406" y1="1046" x2="486" y2="1046"/><line x1="715" y1="1046" x2="797" y2="1046"/></g>
    <path d="M481 1040 l12 6 l-12 6 z M792 1040 l12 6 l-12 6 z" fill="#9a9aa0"/>
  </svg>

  <p class="step-text" style="left:156px;top:1127px">Schedule an appointment to go through the basics of what you need and to find out if we are a good fit to work together</p>
  <p class="step-text" style="left:466px;top:1127px">Work with our team to build out your customer journey and selling system</p>
  <p class="step-text" style="left:775px;top:1127px">Execute and enjoy the extra revenue!</p>

  <p class="para" style="top:1235px;color:#111">So, Schedule Your Appointment Today.</p>
  <p class="para" style="top:1268px">And in the meantime, checkout our Chatterbook ads checklist. So you can stop any poor running campaigns and fill in the gaps where they are needed.</p>
  <a class="btn" style="left:519px;top:1337px;width:162px;height:40px;font-size:19px">Get Started</a>
</section>

<!-- TESTIMONIALS -->
<section class="reviews" role="img" aria-label="Dimmed photo of a team meeting in an office"></section>
<h2 class="section-title" style="top:1524px;color:var(--white);font-size:33px">What Others Are Saying…</h2>
<div class="rule" style="top:1580px"></div>

<div class="slider-btn" style="left:99px;top:1791px;background:#8a8d94;color:#333">◀</div>
<div class="slider-btn" style="left:1058px;top:1792px;background:#f2f4f8;color:#555">▶</div>

<article class="card" style="left:191px;top:1655px;width:258px;height:317px">
  <div class="quote">“</div>
  <p>Lorem ipsum dolor sit amet, consectetuer adipiscing elit, sed diam nonummy nibh euismod tincidunt ut laoreet dolore magna aliquam erat volutpat. Ut wisi enim ad minim veniam, quis nostrud exerci tation.</p>
  <svg class="wave" width="258" height="110" viewBox="0 0 258 110"><path d="M0 20 C60 0 110 30 160 22 C200 15 230 5 258 12 V110 H0 Z" fill="var(--blue)"/></svg>
  <div class="avatar" style="left:94px;top:170px" role="img" aria-label="Portrait of reviewer"></div>
  <div class="name" style="top:258px">Marla Quenby</div>
  <div class="co" style="top:283px">Company Name</div>
</article>

<article class="card" style="left:471px;top:1619px;width:258px;height:353px">
  <div class="quote">“</div>
  <p style="top:44px">Lorem ipsum dolor sit amet, consectetuer adipiscing elit, sed diam nonummy nib er adipiscing elit, sed diam nonummy nibh euismod tincidunt ut laoreet dolore mah euismod tincidunt ut laoreet dolore magna aliquam erat volutpat. Ut wisi enim ad minim veniam, quis nostrud exerci tation.</p>
  <svg class="wave" width="258" height="120" viewBox="0 0 258 120"><path d="M0 14 C50 0 100 28 150 26 C200 24 230 8 258 14 V120 H0 Z" fill="var(--green)"/></svg>
  <div class="avatar" style="left:94px;top:206px;background:#8c6a55" role="img" aria-label="Portrait of reviewer"></div>
  <div class="name" style="top:294px">Tovin Rask</div>
  <div class="co" style="top:319px">Company Name</div>
</article>

<article class="card" style="left:749px;top:1655px;width:257px;height:317px">
  <div class="quote">“</div>
  <p>Lorem ipsum dolor sit amet, consectetuer adipiscing elit, sed diam nonummy nibh euismod tincidunt ut laoreet dolore magna aliquam erat volutpat. Ut wisi enim ad minim veniam, quis nostrud exerci tation.</p>
  <svg class="wave" width="257" height="110" viewBox="0 0 257 110"><path d="M0 12 C40 4 90 28 140 24 C190 20 225 4 257 10 V110 H0 Z" fill="var(--yellow)"/></svg>
  <div class="avatar" style="left:94px;top:171px;background:#c9a592" role="img" aria-label="Portrait of reviewer"></div>
  <div class="name" style="top:262px">Delia Strand</div>
  <div class="co" style="top:285px">Company Name</div>
</article>

<!-- FEATURED -->
<h2 class="section-title" style="top:2116px">As Featured On</h2>
<div class="rule" style="top:2170px"></div>
<div class="feature-box" style="left:142px">Verdanto</div>
<div class="feature-box" style="left:299px">Verdanto</div>
<div class="feature-box" style="left:456px">QuillPress</div>
<div class="feature-box" style="left:614px">Bouncely</div>
<div class="feature-box" style="left:771px">PolyLingo</div>
<div class="feature-box" style="left:929px">PolyLingo</div>

<!-- FOOTER -->
<footer class="footer" role="img" aria-label="Dark city skyline photo behind footer"></footer>
<div class="foot-h" style="left:146px">Quick Links</div>
<div class="foot-h" style="left:294px">Other Links</div>
<div class="foot-h" style="left:493px">Contact Details</div>
<div class="foot-link" style="left:146px;top:2456px">Home</div>
<div class="foot-link" style="left:146px;top:2481px">About</div>
<div class="foot-link" style="left:146px;top:2508px">Case Studies</div>
<div class="foot-link" style="left:146px;top:2533px">Contact Us</div>
<div class="foot-link" style="left:294px;top:2456px">Lorem Ispum</div>
<div class="foot-link" style="left:294px;top:2481px">Lorem Ispum</div>
<div class="foot-link" style="left:294px;top:2507px">Lorem Ispum</div>
<div class="foot-link" style="left:294px;top:2532px">Lorem Ispum</div>

<svg class="abs" style="left:490px;top:2455px" width="24" height="28" viewBox="0 0 24 28"><path d="M12 2 a8 8 0 0 1 8 8 c0 6 -8 15 -8 15 s-8 -9 -8 -15 a8 8 0 0 1 8 -8z" fill="none" stroke="#2f7de0" stroke-width="1.8"/><circle cx="12" cy="10" r="3" fill="none" stroke="#2f7de0" stroke-width="1.8"/></svg>
<div class="foot-link" style="left:528px;top:2456px;line-height:18px">Street Name, City Name<br>State Zipcode</div>
<svg class="abs" style="left:705px;top:2460px" width="24" height="22" viewBox="0 0 24 22"><rect x="2" y="4" width="20" height="15" fill="none" stroke="#2f7de0" stroke-width="1.8"/><path d="M2 5 l10 8 l10 -8" fill="none" stroke="#2f7de0" stroke-width="1.8"/></svg>
<div class="foot-link" style="left:736px;top:2464px;line-height:18px">Email Us<br>inquiry@emberpixelry.com</div>
<svg class="abs" style="left:917px;top:2460px" width="24" height="24" viewBox="0 0 24 24"><path d="M5 3 l4 0 l2 5 l-3 2 c1 3 3 5 6 6 l2 -3 l5 2 l0 4 c-9 1 -17 -7 -16 -16z" fill="none" stroke="#2f7de0" stroke-width="1.8"/></svg>
<div class="foot-link" style="left:949px;top:2464px;line-height:18px">Call Us<br>123.456.7890</div>

<div class="brand" style="left:493px;top:2528px;font-size:26px"><span class="brand-dot" style="width:12px;height:12px"></span>EMBERPIXELRY</div>
<div class="foot-link" style="left:817px;top:2537px">Follow Us On</div>
<div class="social" style="left:900px"></div>
<div class="social" style="left:929px"></div>
<div class="social" style="left:959px"></div>

<div class="band">Copyright © 2020 EmberPixelry. All Rights Reserved. Terms of Service &nbsp; | &nbsp; Privacy Policy</div>

</body>
</html>
```